Copperleaf Motorized Shade Business Card

Hello, we've had our logo made. Now we are looking for a clean and cool looking business card. One side can just be the logo with any design elements that might look good with it. The other side will be Name, Phone Number and Email. There will not be an address on the card.

```html
<!DOCTYPE html>
<html lang="en">
<head>
<meta charset="utf-8">
<title>Copperleaf Motorized Shade – Business Card</title>
<link rel="stylesheet" href="https://fonts.googleapis.com/css2?family=Oswald:wght@500;600&family=Montserrat:wght@500;600&display=swap">
<style>
  :root {
    --page-bg: #e3e3e3;
    --card-white: #ffffff;
    --sand: #fff4e6;
    --navy: #0d3f73;
    --ink: #111111;
    --cyan-text: #1fb8ee;
    --rule: #9a9a9a;
    --sea-light: #d8fbfd;
    --sea-mid: #4cdaf7;
    --sea-deep: #0bb0ec;
    --mist-light: #eafcfe;
    --mist-mid: #baf1fd;
    --mist-deep: #8edbf8;
  }
  * { box-sizing: border-box; margin: 0; padding: 0; }
  html, body { width: 1200px; height: 1200px; overflow: hidden; }
  body { background: var(--page-bg); position: relative; }

  .card {
    position: absolute;
    left: 130px;
    width: 940px;
    height: 530px;
    background: var(--card-white);
    box-shadow: 0 2px 10px rgba(0,0,0,0.08);
  }
  .card--front { top: 40px; }
  .card--back { top: 630px; }

  .card__panel {
    position: absolute;
    inset: 24px;
    overflow: hidden;
    background: linear-gradient(to bottom, var(--sand) 0%, #ffffff 25%, #ffffff 100%);
  }

  .card__sea {
    position: absolute;
    left: 0; right: 0; bottom: 0;
  }
  .card--front .card__sea {
    top: 120px;
    background: linear-gradient(to bottom, var(--sea-light) 0%, var(--sea-mid) 55%, var(--sea-deep) 100%);
  }
  .card--back .card__sea {
    top: 130px;
    background: linear-gradient(to bottom, var(--mist-light) 0%, var(--mist-mid) 55%, var(--mist-deep) 100%);
  }

  .brand {
    position: absolute;
    top: 60px;
    left: 0; right: 0;
    text-align: center;
  }
  .brand__row {
    display: inline-flex;
    align-items: flex-end;
    gap: 14px;
  }
  .brand__mark {
    width: 36px;
    height: 36px;
    background: var(--navy);
    margin-bottom: 12px;
  }
  .brand__name {
    font-family: "Oswald", sans-serif;
    font-weight: 600;
    font-size: 88px;
    line-height: 1;
    color: var(--navy);
    letter-spacing: 1px;
  }
  .brand__tagline {
    margin-top: 8px;
    font-family: "Montserrat", sans-serif;
    font-weight: 600;
    font-size: 15px;
    letter-spacing: 5px;
    color: var(--cyan-text);
  }

  .contact-block {
    position: absolute;
    top: 82px;
    left: 0; right: 0;
    text-align: center;
  }
  .contact-block__name {
    font-family: "Oswald", sans-serif;
    font-weight: 500;
    font-size: 52px;
    line-height: 1;
    color: var(--ink);
    letter-spacing: 2px;
  }
  .contact-block__tagline {
    margin-top: 8px;
    font-family: "Montserrat", sans-serif;
    font-weight: 500;
    font-size: 19px;
    color: var(--ink);
  }
  .contact-block__rule {
    width: 440px;
    height: 1px;
    background: var(--rule);
    margin: 22px auto 16px;
  }
  .contact-list {
    display: inline-flex;
    align-items: center;
    gap: 14px;
    list-style: none;
    font-family: "Montserrat", sans-serif;
    font-weight: 500;
    font-size: 18px;
    color: var(--ink);
  }
  .contact-list__item { display: inline-flex; align-items: center; gap: 8px; }
  .contact-list__divider { width: 1px; height: 28px; background: var(--ink); }
  .contact-list__icon { width: 22px; height: 22px; }
</style>
</head>
<body>

  <section class="card card--front" aria-label="Card front">
    <div class="card__panel">
      <div class="card__sea" role="img" aria-label="Decorative layered blue wave pattern"></div>
      <div class="brand">
        <div class="brand__row">
          <span class="brand__mark"></span>
          <span class="brand__name">COPPERLEAF</span>
        </div>
        <p class="brand__tagline">MOTORIZED SHADES</p>
      </div>
    </div>
  </section>

  <section class="card card--back" aria-label="Card back">
    <div class="card__panel">
      <div class="card__sea" role="img" aria-label="Decorative pale blue wave pattern"></div>
      <div class="contact-block">
        <h1 class="contact-block__name">COPPERLEAF</h1>
        <p class="contact-block__tagline">Motorized Shades</p>
        <div class="contact-block__rule"></div>
        <ul class="contact-list">
          <li class="contact-list__item">
            <svg class="contact-list__icon" viewBox="0 0 24 24" aria-hidden="true">
              <rect x="7" y="2" width="10" height="20" rx="1.5" fill="none" stroke="#111" stroke-width="1.4"/>
              <line x1="10.5" y1="19" x2="13.5" y2="19" stroke="#111" stroke-width="1.4"/>
            </svg>
            +91 9876501234
          </li>
          <li class="contact-list__divider" aria-hidden="true"></li>
          <li class="contact-list__item">
            <svg class="contact-list__icon" viewBox="0 0 24 24" aria-hidden="true">
              <rect x="2" y="5" width="20" height="14" fill="none" stroke="#111" stroke-width="1.3"/>
              <polyline points="2,5 12,13 22,5" fill="none" stroke="#111" stroke-width="1.3"/>
            </svg>
            hello@copperleafmail.com
          </li>
        </ul>
      </div>
    </div>
  </section>

</body>
</html>
```